DL Flyer for conservation/restoration business

I am an objects conservator and run a business called RelicCare Studio. I specialise in conserving and restoring 3 dimensional artworks and artefacts in Perth, Western Australia. I dont work on paintings, paper or textiles but pretty much everything else such as sculptures, metal, wood, ceramics etc. So far I have been reasonably successful in marketing to small museums and councils. However, I would like to pick up some more work from private individuals living in the more affluent areas of Perth.

I would like to have a DL flyer designed to do a letterbox drop in my target areas. I would like something professional and eyecatching that wont get thrown away. Also it will make the business look trustworthy.

I would like to have something that will go with my existing logo if possible.

Target Market(s)

wealthy individuals over 50 who enjoy collecting art / antiques

Industry/Entity Type

Marketing

Requirements
Must have
• I would like a good background image or images of suitable artworks/ artefacts/ conservator at work (hands only). Also include my logo as the business name.

I am happy to take advice on advertising, but my preference is for the text in the attached word file (order can be rearranged):

I would like to be able to edit the flyer if necessary at a later date, and would like it to be compatible with MS Publisher.
Should not have
• Do not include any images of paintings, textiles, paper or books.

```html
<!DOCTYPE html>
<html lang="en">
<head>
<meta charset="utf-8">
<title>RelicCare Studio – DL Flyer</title>
<link rel="stylesheet" href="https://fonts.googleapis.com/css2?family=Arimo:wght@400;700&family=Questrial&display=swap">
<style>
  :root {
    --page-bg: #f2f2f2;
    --paper: #ffffff;
    --panel: #eef2f3;
    --edge: #8a8a8a;
    --top-bar: #3a2a22;
    --ink-grey: #6d6d6d;
    --brand-blue: #1f3fd6;
    --brand-red: #b3122a;
    --ink-black: #111111;
    --photo-deep: #2d3f9a;
    --photo-mid: #6a7fc8;
    --photo-warm: #b9824d;
    --photo-dark: #3b2a22;
  }
  * { box-sizing: border-box; margin: 0; padding: 0; }
  html, body {
    width: 886px; height: 1200px; overflow: hidden;
    background: var(--page-bg);
  }
  .flyer {
    position: absolute; left: 169px; top: 15px;
    width: 548px; height: 1170px;
    background: var(--panel);
    border: 1px solid var(--edge);
    overflow: hidden;
    font-family: "Questrial", "Century Gothic", sans-serif;
  }
  .flyer__bar {
    position: absolute; left: 0; top: 0; width: 100%; height: 10px;
    background: var(--top-bar);
  }
  .header {
    position: absolute; left: 0; top: 10px; width: 100%; height: 136px;
    background: var(--paper);
  }
  .contact {
    position: absolute; left: 14px; top: 22px;
    color: var(--ink-grey); font-size: 19px; line-height: 25px;
  }
  .contact__phone { font-size: 21px; }
  .contact__email { font-size: 18px; }
  .brand {
    position: absolute; left: 262px; top: 32px;
    display: flex; align-items: center; gap: 10px;
  }
  .brand__mark {
    width: 30px; height: 30px; background: var(--brand-blue);
  }
  .brand__name {
    font-family: "Arimo", Arial, sans-serif; font-weight: 700;
    font-size: 31px; color: var(--brand-red); letter-spacing: 0.2px;
  }
  .hero {
    position: absolute; left: 0; top: 146px; width: 548px; height: 600px;
  }
  .headline {
    position: absolute; left: 0; top: 0; width: 100%;
    font-family: "Arimo", Arial, sans-serif; font-weight: 700;
    font-size: 64px; line-height: 66px; color: var(--paper);
    text-shadow:
      2px 0 0 var(--brand-blue), -2px 0 0 var(--brand-blue),
      0 2px 0 var(--brand-blue), 0 -2px 0 var(--brand-blue),
      2px 2px 0 var(--brand-blue), -2px -2px 0 var(--brand-blue),
      2px -2px 0 var(--brand-blue), -2px 2px 0 var(--brand-blue);
  }
  .headline__line { position: absolute; white-space: nowrap; }
  .headline__line--1 { left: 34px; top: 132px; }
  .headline__line--2 { left: 75px; top: 201px; }
  .headline__line--3 { left: 34px; top: 266px; }
  .headline__line--4 { left: 194px; top: 334px; }
  .services {
    position: absolute; left: 0; top: 0; width: 100%;
  }
  .services__title {
    position: absolute; font-family: "Arimo", Arial, sans-serif; font-weight: 700;
    font-size: 22px; color: var(--brand-blue); white-space: nowrap;
  }
  .services__title--1 { left: 32px; top: 710px; }
  .services__title--2 { left: 36px; top: 749px; }
  .services__list {
    position: absolute; left: 22px; top: 781px; width: 510px;
    list-style: none; color: var(--brand-red); font-size: 21.5px; line-height: 33px;
  }
  .services__item { position: relative; padding-left: 18px; }
  .services__item::before {
    content: "•"; position: absolute; left: 0; top: 0;
  }
  .credentials {
    position: absolute; left: 36px; top: 989px;
    font-family: "Arimo", Arial, sans-serif; font-weight: 700;
    font-size: 19px; line-height: 23.3px; color: var(--brand-blue);
  }
  .website {
    position: absolute; left: 28px; top: 1115px;
    font-family: "Arimo", Arial, sans-serif; font-weight: 700;
    font-size: 29px; color: var(--ink-black); white-space: nowrap;
  }
</style>
</head>
<body>
  <main class="flyer">
    <div class="flyer__bar"></div>

    <header class="header">
      <div class="contact">
        <p class="contact__name">Helena Marsh</p>
        <p class="contact__phone">9555 0142</p>
        <p class="contact__phone">0400 555 318</p>
        <p class="contact__email">studio@reliccarestudio.com</p>
      </div>
      <div class="brand">
        <span class="brand__mark"></span>
        <span class="brand__name">RelicCare Studio</span>
      </div>
    </header>

    <svg class="hero" viewBox="0 0 548 600" width="548" height="600" aria-hidden="false">
      <defs>
        <linearGradient id="photoTone" x1="0" y1="0" x2="1" y2="1">
          <stop offset="0" stop-color="var(--photo-dark)"/>
          <stop offset="0.25" stop-color="var(--photo-warm)"/>
          <stop offset="0.5" stop-color="var(--photo-mid)"/>
          <stop offset="0.75" stop-color="var(--photo-deep)"/>
          <stop offset="1" stop-color="var(--photo-warm)"/>
        </linearGradient>
      </defs>
      <rect role="img" aria-label="Photograph of ornate hand-painted blue enamel vases and bowls on display"
            x="0" y="0" width="548" height="600" fill="url(#photoTone)"/>
      <path d="M0 378 C 150 500, 350 590, 548 596 L548 600 L0 600 Z" fill="var(--panel)"/>
    </svg>

    <h1 class="headline">
      <span class="headline__line headline__line--1">Perth’s</span>
      <span class="headline__line headline__line--2">most trusted</span>
      <span class="headline__line headline__line--3">conservation</span>
      <span class="headline__line headline__line--4">service</span>
    </h1>

    <section class="services">
      <h2 class="services__title services__title--1">Conservation and</h2>
      <h2 class="services__title services__title--2">restoration of objects including:</h2>
      <ul class="services__list">
        <li class="services__item">Historical items, antiques, ceramics<br>and sculpture</li>
        <li class="services__item">Custom made display fittings and supports.</li>
        <li class="services__item">Free advice on storage and display<br>techniques to help preserve your<br>treasured items.</li>
      </ul>
    </section>

    <p class="credentials">
      University trained conservator with<br>
      over 20 years’ experience in major galleries<br>
      and museums.<br>
      Offering free quotes in your area on:
    </p>

    <p class="website">www.reliccarestudio.com</p>
  </main>
</body>
</html>
```